Premium CBD/Hemp company needs packaging and label design

Verdant Oakfield, a premium CBD/Hemp company based in Scottsdale, Arizona is in need of a packaging and label design. We are launching with our flagship product which will be a 30 count capsule and will come in three functions: Pain Relief, Anxiety Support, and Sleep Support. For the purpose of this contest, please design packaging and label for our Anxiety Support product. Our products are physician formulated and all natural. Our main ingredient is CBD/Hemp and is complemented by specific herbs that synergistically work together to give the customer the most effective and desired result. We would like our branding to have a pharmaceutical look and feel with a focus on trust and transparency. We have uploaded our company logo that is to be used on both the packaging and label. We have also uploaded an executed branding questionnaire that will guide you to exactly what we are seeking to achieve as to the look and feel of our brand. Please feel free to contact us with any questions that you may have. The winner of this contest will have the opportunity to work with us on future projects as we will need packaging and label design for our entire Verdant Oakfield product line.

Target Market(s)

See attached branding questionnaire

Industry/Entity Type

Health And Wellness

Font styles to use
Sans Serif

Colors

Designer to choose colors to be used in the design.

Requirements
Must have
• See attached branding questionnaire; Please superimpose labels onto a cobalt blue capsule bottle (see attached)
• >>UPON REVIEW of the FIRST 8 designs, we really like the silver, mildly metallic label background in DESIGN # 21300528, we do not want metalic lettering as that would not look very "Pharmaceutical"
• >>We are in search of a look that is a bit more "Pharmaceutical" than a look that would be more commonly found in a Supplement Store
Nice to have
• "See attached branding questionnaire
Should not have
• See attached branding questionnaire; NO marijuana or cannabis plant on the packaging or label

```html
<!DOCTYPE html>
<html lang="en">
<head>
<meta charset="utf-8">
<title>Verdant Oakfield – Hemp Extract Packaging</title>
<link rel="stylesheet" href="https://fonts.googleapis.com/css2?family=Poppins:wght@500;600&family=Roboto+Condensed:wght@400;700&family=Roboto:wght@400&display=swap">
<style>
  :root{
    --bg:#eceef0;
    --cobalt:#1b2fb0;
    --cobalt-dark:#101f86;
    --silver-light:#f7f8f9;
    --silver:#dfe2e5;
    --silver-dark:#a9aeb4;
    --ink:#3a3d42;
    --green:#1f8a3a;
    --green-dark:#146b2a;
    --white:#ffffff;
  }
  *{box-sizing:border-box;margin:0;padding:0}
  html,body{width:1200px;height:1200px;overflow:hidden}
  body{background:var(--bg);position:relative;font-family:"Roboto",sans-serif}

  /* ---------- Bottle label (flat) ---------- */
  .label{
    position:absolute;left:30px;top:330px;width:560px;height:540px;
    background:linear-gradient(90deg,var(--silver) 0%,var(--silver-light) 45%,var(--white) 60%,var(--silver) 100%);
    border-top:14px solid var(--cobalt);border-bottom:14px solid var(--cobalt);
  }
  .brand{position:absolute;display:flex;align-items:center;gap:14px}
  .brand-mark{width:58px;height:58px;border:3px solid var(--cobalt);border-radius:50%;flex:none}
  .brand-name{font-family:"Roboto Condensed",sans-serif;font-weight:400;color:var(--cobalt);font-size:34px;letter-spacing:1px;line-height:1}
  .label .brand{left:95px;top:40px}

  .leaf-art{position:absolute;border-radius:50% 50% 8px 8px;
    background:radial-gradient(ellipse at 50% 60%,#c3c7cc 0%,#e4e6e9 55%,rgba(255,255,255,0) 75%)}
  .label .leaf-art{left:165px;top:140px;width:230px;height:110px}

  .banner{position:absolute;left:0;width:100%}
  .banner svg{display:block;width:100%;height:100%}
  .banner-text{position:absolute;inset:0;display:flex;align-items:center;justify-content:center;
    font-family:"Poppins",sans-serif;font-weight:500;color:var(--white);letter-spacing:.5px}
  .banner-text b{font-weight:600;margin-right:12px}
  .label .banner{top:250px;height:90px}
  .label .banner-text{font-size:40px}

  .benefits{position:absolute;left:14px;top:370px;list-style:none;font-family:"Roboto Condensed",sans-serif;color:var(--ink);font-size:17px}
  .benefits li{width:120px;padding:6px 0 7px;border-bottom:1px solid var(--silver-dark)}
  .benefits li:last-child{border-bottom:none}

  .strength{position:absolute;text-align:center;font-family:"Roboto Condensed",sans-serif;font-weight:700}
  .strength .mg{color:#55585d;font-size:38px;line-height:1}
  .strength .mg small{font-size:20px;font-weight:400}
  .strength .cbd{color:var(--cobalt);font-size:74px;line-height:.95;letter-spacing:1px}
  .label .strength{left:188px;top:350px;width:130px}

  .badge{position:absolute;border-radius:50%;border:3px solid var(--green);
    box-shadow:inset 0 0 0 14px var(--white),inset 0 0 0 16px var(--green)}
  .label .badge{left:400px;top:370px;width:100px;height:100px}

  .count-tab{position:absolute;height:46px;display:flex;align-items:center;justify-content:center;
    font-family:"Roboto Condensed",sans-serif;font-size:24px;color:var(--ink);letter-spacing:1px;
    background:linear-gradient(180deg,#e6e8ea,#c9ccd0);clip-path:polygon(8% 0,92% 0,100% 100%,0 100%)}
  .label .count-tab{left:150px;top:466px;width:260px}

  /* ---------- Carton side panel ---------- */
  .carton-side{
    position:absolute;left:615px;top:180px;width:200px;height:840px;
    background:linear-gradient(180deg,var(--cobalt) 0%,var(--cobalt-dark) 100%);overflow:hidden;
  }
  .carton-side .leaf-art{left:0;top:20px;width:120px;height:200px;border-radius:0 60% 60% 0;
    background:radial-gradient(ellipse at 30% 40%,rgba(230,233,238,.7) 0%,rgba(200,205,215,.35) 45%,rgba(255,255,255,0) 75%)}
  .side-title{position:absolute;left:96px;top:400px;transform:translate(-50%,-50%) rotate(-90deg);white-space:nowrap;
    font-family:"Poppins",sans-serif;font-weight:500;color:var(--white);font-size:38px;letter-spacing:1px}
  .side-title b{font-weight:600;margin-right:10px}
  .side-copy{position:absolute;left:16px;top:620px;width:170px;color:var(--white);font-size:11px;line-height:1.6;text-align:justify}

  /* ---------- Carton front panel ---------- */
  .carton-front{
    position:absolute;left:815px;top:180px;width:360px;height:840px;
    background:linear-gradient(90deg,var(--silver) 0%,var(--silver-light) 40%,var(--white) 60%,var(--silver) 100%);
  }
  .carton-front .brand{left:0;right:0;top:60px;flex-direction:column;gap:14px}
  .carton-front .brand-mark{width:76px;height:76px}
  .carton-front .brand-name{font-size:36px;text-align:center}
  .carton-front .leaf-art{left:60px;top:230px;width:240px;height:170px}
  .carton-front .banner{top:410px;height:100px}
  .carton-front .banner-text{font-size:40px}
  .spectrum{position:absolute;left:0;right:0;top:540px;text-align:center;font-family:"Roboto Condensed",sans-serif;
    font-size:22px;letter-spacing:3px;color:var(--ink);line-height:1}
  .rule{position:absolute;left:150px;top:585px;width:70px;height:3px;background:var(--silver-dark)}
  .icons{position:absolute;left:35px;top:605px;display:flex;flex-direction:column;gap:14px;list-style:none}
  .icons li{width:56px;height:56px;border-radius:50%;background:radial-gradient(circle,var(--green) 55%,var(--green-dark) 100%);
    border:3px solid var(--white);box-shadow:0 0 0 2px var(--green);display:flex;align-items:center;justify-content:center}
  .icons svg{width:30px;height:30px}
  .carton-front .strength{left:120px;top:625px;width:120px}
  .carton-front .strength .cbd{font-size:72px}
  .carton-front .badge{left:255px;top:640px;width:92px;height:92px}
  .carton-front .count-tab{left:95px;top:775px;width:190px;font-size:22px}
</style>
</head>
<body>

<section class="label" aria-label="Bottle label">
  <div class="brand">
    <span class="brand-mark"></span>
    <span class="brand-name">Verdant Oakfield</span>
  </div>
  <div class="leaf-art" role="img" aria-label="Silver falling leaves illustration"></div>
  <div class="banner">
    <svg viewBox="0 0 560 100" preserveAspectRatio="none" aria-hidden="true">
      <rect x="0" y="47" width="560" height="6" fill="var(--cobalt)"/>
      <polygon points="70,50 100,8 460,8 490,50 460,92 100,92" fill="var(--silver-dark)"/>
      <polygon points="78,50 105,14 455,14 482,50 455,86 105,86" fill="var(--cobalt)"/>
    </svg>
    <div class="banner-text"><b>Hemp</b>Extract</div>
  </div>
  <ul class="benefits">
    <li>Pain Relief</li>
    <li>Anxiety Support</li>
    <li>Sleep Support</li>
  </ul>
  <div class="strength">
    <div class="mg">3000<small>MG</small></div>
    <div class="cbd">CBD</div>
  </div>
  <div class="badge" role="img" aria-label="Natural formula seal"></div>
  <div class="count-tab">30 CAPSULES</div>
</section>

<section class="carton-side" aria-label="Carton side panel">
  <div class="leaf-art" role="img" aria-label="Silver leaves illustration"></div>
  <div class="side-title"><b>Hemp</b>Extract</div>
  <p class="side-copy">Each capsule delivers a balanced dose of full spectrum hemp extract blended with calming herbs. Take one capsule daily with water or as directed by your physician. Store in a cool, dry place.</p>
</section>

<section class="carton-front" aria-label="Carton front panel">
  <div class="brand">
    <span class="brand-mark"></span>
    <span class="brand-name">Verdant Oakfield</span>
  </div>
  <div class="leaf-art" role="img" aria-label="Silver falling leaves illustration"></div>
  <div class="banner">
    <svg viewBox="0 0 360 110" preserveAspectRatio="none" aria-hidden="true">
      <rect x="0" y="52" width="360" height="6" fill="var(--cobalt)"/>
      <polygon points="16,55 44,8 316,8 344,55 316,102 44,102" fill="var(--silver-dark)"/>
      <polygon points="24,55 50,14 310,14 336,55 310,96 50,96" fill="var(--cobalt)"/>
    </svg>
    <div class="banner-text"><b>Hemp</b>Extract</div>
  </div>
  <div class="spectrum">FULL SPECTRUM</div>
  <div class="rule"></div>
  <ul class="icons">
    <li aria-label="Relief">
      <svg viewBox="0 0 30 30"><circle cx="15" cy="15" r="11" fill="none" stroke="#fff" stroke-width="2.5"/><line x1="7" y1="23" x2="23" y2="7" stroke="#fff" stroke-width="2.5"/></svg>
    </li>
    <li aria-label="Calm">
      <svg viewBox="0 0 30 30"><circle cx="15" cy="15" r="10" fill="none" stroke="#fff" stroke-width="2.5"/><line x1="15" y1="6" x2="15" y2="24" stroke="#fff" stroke-width="2"/></svg>
    </li>
    <li aria-label="Sleep">
      <svg viewBox="0 0 30 30"><path d="M19 5a11 11 0 1 0 6 15A9 9 0 0 1 19 5z" fill="#fff"/></svg>
    </li>
  </ul>
  <div class="strength">
    <div class="mg">3000<small>MG</small></div>
    <div class="cbd">CBD</div>
  </div>
  <div class="badge" role="img" aria-label="Natural formula seal"></div>
  <div class="count-tab">30 CAPSULES</div>
</section>

</body>
</html>
```